WordPress Website for Pain Relief Clinic

I need a WordPress website designed for my laser pain relief clinic. It needs to be a professional, responsive design with 7 pages: Home, Why Choose Us, Treatable Conditions, Testimonials, FAQ, Franchising, Contact Us. Here is logo: https://files.brivoltcdn.com/media.t-w-e-n.com/sitebuilder/472/CalvexaLogoHighQuality.png

Target Market(s)

people with pain,elderly adults,injuries,soreness

Industry/Entity Type

Clinic

Number of Pages Required

5+ page

Colors
0792cd
85abd2

```html
<!DOCTYPE html>
<html lang="en">
<head>
<meta charset="utf-8">
<title>Calvexa Pain Treatment Center</title>
<link rel="stylesheet" href="https://fonts.googleapis.com/css2?family=Open+Sans:wght@400;600;700;800&display=swap">
<style>
:root{
  --blue:#0792cd;
  --blue-soft:#85abd2;
  --blue-pale:#dcebf6;
  --red:#c8121d;
  --dark:#3a3a3a;
  --footer:#262626;
  --footer-deep:#1a1a1a;
  --ink:#333;
  --muted:#8a8a8a;
  --grey-bg:#f2f2f2;
  --white:#fff;
}
*{box-sizing:border-box;margin:0;padding:0}
html,body{width:1200px;height:3536px;overflow:hidden}
body{font-family:"Open Sans",Arial,sans-serif;color:var(--ink);background:var(--white);position:relative}
.section{position:absolute;left:0;width:1200px}
.abs{position:absolute}

/* header */
.site-header{top:0;height:135px}
.brand{left:110px;top:32px;display:flex;align-items:center;gap:14px}
.brand-mark{width:22px;height:22px;background:var(--blue);border-radius:50%}
.brand-name{font-size:58px;font-weight:800;color:var(--blue);letter-spacing:-1px;line-height:1}
.header-phone{left:620px;top:50px;display:flex;align-items:center;gap:14px;font-size:30px;font-weight:600;color:var(--ink)}
.social{left:900px;top:50px;display:flex;gap:8px}
.social span{width:32px;height:32px;border-radius:3px;background:var(--blue)}
.social span:nth-child(3){background:var(--blue-soft)}
.social span:nth-child(4),.social span:nth-child(5){background:var(--red)}

.main-nav{top:135px;height:44px;background:var(--dark);display:flex;padding-left:110px}
.main-nav a{color:var(--white);font-size:15px;font-weight:600;text-decoration:none;padding:0 22px;line-height:44px;text-transform:uppercase}
.main-nav a.active{background:var(--blue)}

/* hero */
.hero{top:179px;height:581px;background:linear-gradient(110deg,#e9eef2 0%,#f6f4f1 40%,#d9dde0 70%,#b9a596 100%)}
.hero-panel{left:660px;top:145px;width:340px;height:220px;background:rgba(7,146,205,.92);padding:24px 26px;color:var(--white)}
.hero-panel h1{font-size:31px;font-weight:700;line-height:1.15;text-transform:uppercase}
.hero-panel p{font-size:14px;line-height:1.35;margin-top:10px}
.btn{display:inline-block;background:var(--red);color:var(--white);font-size:14px;font-weight:600;padding:8px 18px;border-radius:2px}
.hero-panel .btn{margin-top:14px}

/* what we do */
.services{top:760px;height:440px;text-align:center}
.section-title{font-size:40px;font-weight:600;color:var(--ink)}
.section-sub{font-size:14px;color:var(--muted);line-height:1.5;margin:14px auto 0;width:620px}
.services .section-title{margin-top:52px}
.service-row{display:flex;justify-content:center;gap:50px;margin-top:40px}
.service{width:200px;height:200px;border-radius:50%;border:6px solid #e3e3e3;overflow:hidden;position:relative;background:linear-gradient(160deg,#e8d6c8,#b99a86)}
.service span{position:absolute;left:0;right:0;bottom:46px;background:rgba(40,40,40,.82);color:var(--white);font-size:17px;font-weight:700;padding:6px 0}

/* about */
.about{top:1200px;height:430px;background:var(--grey-bg)}
.about-photo{left:110px;top:70px;width:360px;height:270px;border:8px solid var(--white);box-shadow:0 2px 8px rgba(0,0,0,.25);transform:rotate(-3deg);background:linear-gradient(135deg,#cfe4f3,#f2f7fb 50%,#7fb2d8)}
.about-copy{left:520px;top:68px;width:570px}
.about-copy h2{font-size:32px;font-weight:600}
.about-copy p{font-size:14px;color:#666;line-height:1.55;margin-top:14px}
.about-copy .btn{margin-top:18px}

/* conditions + video */
.conditions{top:1630px;height:430px}
.conditions h3,.video h3{font-size:32px;font-weight:600}
.conditions-list{left:110px;top:56px}
.cond-cols{display:flex;gap:40px;margin-top:22px}
.cond-cols ul{list-style:none}
.cond-cols li{display:flex;align-items:center;gap:12px;font-size:14px;color:#555;height:37px}
.tick{width:20px;height:20px;background:var(--blue);border-radius:2px;display:flex;align-items:center;justify-content:center}
.video{left:660px;top:56px;width:430px}
.video-frame{margin-top:22px;height:256px;background:linear-gradient(135deg,#6b5a50,#2b2422);position:relative}
.video-bar{position:absolute;left:0;right:0;bottom:0;height:30px;background:#111}
.video-bar i{position:absolute;left:60px;top:13px;width:200px;height:4px;background:var(--red)}

/* appointment */
.appointment{top:2060px;height:500px;background:linear-gradient(100deg,#eef6fb 0%,#cfe3f2 50%,#a9cbe6 100%)}
.doctor{left:110px;top:40px;width:380px;height:460px;background:linear-gradient(180deg,#f4ede6,#e1e7ec 60%,#c7d7e4)}
.booking{left:570px;top:60px;width:520px}
.booking h3{font-size:30px;font-weight:600}
.booking p{font-size:14px;color:#555;margin-top:4px}
.fields{display:grid;grid-template-columns:1fr 1fr;gap:10px;margin-top:18px}
.field{height:40px;background:rgba(255,255,255,.85);border:1px solid #c6d6e2;font-size:13px;color:#999;padding:10px 12px}
.field.wide{grid-column:span 2}
.field.msg{height:100px}
.submit{margin-top:10px;background:var(--red);color:var(--white);text-align:center;font-size:22px;font-weight:600;height:46px;line-height:46px}

/* testimonials */
.testimonials{top:2560px;height:580px;text-align:center}
.testimonials h2{font-size:38px;font-weight:600;line-height:1.25;margin-top:70px}
.testimonials .link{font-size:14px;color:var(--blue);margin-top:14px}
.rule{width:50px;height:3px;background:var(--blue);margin:10px auto 0}
.avatars{display:flex;justify-content:center;align-items:center;gap:34px;margin-top:40px}
.avatar{width:118px;height:118px;border-radius:50%;border:5px solid #e6e6e6;background:linear-gradient(160deg,#d8cfc8,#8e8680)}
.avatar.active{width:170px;height:170px;border-color:var(--red)}
.arrow{top:370px;width:40px;height:40px;border-radius:50%;background:#e6e6e6;display:flex;align-items:center;justify-content:center}
.t-name{font-size:20px;font-weight:700;color:var(--red);margin-top:18px;text-transform:uppercase}
.t-place{font-size:13px;color:var(--muted)}
.t-quote{font-size:14px;color:#666;line-height:1.55;width:860px;margin:14px auto 0}

/* cta */
.cta{top:3140px;height:160px;background:var(--blue);color:var(--white)}
.cta h2{left:110px;top:46px;font-size:32px;font-weight:700}
.cta p{left:110px;top:92px;font-size:15px}
.cta-phone{left:820px;top:56px;display:flex;align-items:center;gap:18px;font-size:38px;font-weight:600}

/* footer */
.site-footer{top:3300px;height:200px;background:var(--footer);color:#bbb}
.f-col{top:26px}
.f-col h4{color:var(--white);font-size:18px;font-weight:600;margin-bottom:10px}
.f-col li{list-style:none;font-size:13px;line-height:19px}
.follow{display:flex;gap:10px}
.follow span{width:28px;height:28px;border-radius:50%;background:#555}
.follow span:nth-child(2){background:var(--blue)}
.map{left:860px;top:30px;width:230px;height:150px;background:linear-gradient(135deg,#e4e2dc,#cfd3cf)}
.copyright{top:3500px;height:36px;background:var(--footer-deep);color:#999;font-size:12px;line-height:36px}
.copyright span{position:absolute}
</style>
</head>
<body>

<header class="section site-header">
  <div class="abs brand"><span class="brand-mark"></span><span class="brand-name">Calvexa</span></div>
  <div class="abs header-phone">
    <svg width="30" height="30" viewBox="0 0 24 24"><path fill="#0792cd" d="M6.6 10.8a15 15 0 0 0 6.6 6.6l2.2-2.2c.3-.3.7-.4 1-.2 1.1.4 2.3.6 3.6.6.6 0 1 .4 1 1V20c0 .6-.4 1-1 1A17 17 0 0 1 3 4c0-.6.4-1 1-1h3.5c.6 0 1 .4 1 1 0 1.3.2 2.5.6 3.6.1.3 0 .7-.2 1z"/></svg>
    248-555-0142
  </div>
  <div class="abs social" aria-label="Social links"><span></span><span></span><span></span><span></span><span></span></div>
</header>

<nav class="section main-nav">
  <a class="active">Home</a><a>About Us</a><a>Treatable Conditions</a><a>Testimonials</a><a>FAQs</a><a>Franchising</a><a>Contact Us</a>
</nav>

<section class="section hero" role="img" aria-label="Therapist applying laser treatment to a patient's back in a bright clinic">
  <div class="abs hero-panel">
    <h1>Laser Pain Relief Experts</h1>
    <p>Gentle laser therapy that eases pain at its source, so you can get back to the life you enjoy.</p>
    <span class="btn">Learn More</span>
  </div>
</section>

<section class="section services">
  <h2 class="section-title">What We Do</h2>
  <p class="section-sub">We treat joint and muscle pain with safe, drug-free laser care that works fast and fits easily into your busy week.</p>
  <div class="service-row">
    <div class="service" role="img" aria-label="Elbow being held in pain"><span>ELBOW PAIN</span></div>
    <div class="service" role="img" aria-label="Lower back being held in pain"><span>BACK PAIN</span></div>
    <div class="service" role="img" aria-label="Hip being held in pain"><span>HIP PAIN</span></div>
    <div class="service" role="img" aria-label="Knee being held in pain"><span>KNEE PAIN</span></div>
  </div>
</section>

<section class="section about">
  <div class="abs about-photo" role="img" aria-label="Team of clinic doctors and nurses in white coats"></div>
  <div class="abs about-copy">
    <h2>About Laser Pain Relief</h2>
    <p>Our clinic uses focused light energy to calm inflammation, speed tissue repair and reduce pain without surgery or medication. Each session is short, painless and guided by trained staff.</p>
    <p>Most clients notice relief within a few visits. We build a plan around your condition, track your progress and adjust care until you feel strong again.</p>
    <p>From sports injuries to long-term joint soreness, our team is here to help you move freely once more.</p>
    <span class="btn">Read More</span>
  </div>
</section>

<section class="section conditions">
  <div class="abs conditions-list">
    <h3>Treatable Conditions</h3>
    <div class="cond-cols">
      <ul>
        <li><span class="tick"><svg width="12" height="12" viewBox="0 0 12 12"><path d="M2 6l3 3 5-6" stroke="#fff" stroke-width="2" fill="none"/></svg></span>Arthritis Pain</li>
        <li><span class="tick"><svg width="12" height="12" viewBox="0 0 12 12"><path d="M2 6l3 3 5-6" stroke="#fff" stroke-width="2" fill="none"/></svg></span>Neck Pain</li>
        <li><span class="tick"><svg width="12" height="12" viewBox="0 0 12 12"><path d="M2 6l3 3 5-6" stroke="#fff" stroke-width="2" fill="none"/></svg></span>Shoulder Pain</li>
        <li><span class="tick"><svg width="12" height="12" viewBox="0 0 12 12"><path d="M2 6l3 3 5-6" stroke="#fff" stroke-width="2" fill="none"/></svg></span>Tendonitis</li>
        <li><span class="tick"><svg width="12" height="12" viewBox="0 0 12 12"><path d="M2 6l3 3 5-6" stroke="#fff" stroke-width="2" fill="none"/></svg></span>Sciatica</li>
        <li><span class="tick"><svg width="12" height="12" viewBox="0 0 12 12"><path d="M2 6l3 3 5-6" stroke="#fff" stroke-width="2" fill="none"/></svg></span>Plantar Fasciitis</li>
        <li><span class="tick"><svg width="12" height="12" viewBox="0 0 12 12"><path d="M2 6l3 3 5-6" stroke="#fff" stroke-width="2" fill="none"/></svg></span>Sports Injuries</li>
      </ul>
      <ul>
        <li><span class="tick"><svg width="12" height="12" viewBox="0 0 12 12"><path d="M2 6l3 3 5-6" stroke="#fff" stroke-width="2" fill="none"/></svg></span>Carpal Tunnel</li>
        <li><span class="tick"><svg width="12" height="12" viewBox="0 0 12 12"><path d="M2 6l3 3 5-6" stroke="#fff" stroke-width="2" fill="none"/></svg></span>Bursitis</li>
        <li><span class="tick"><svg width="12" height="12" viewBox="0 0 12 12"><path d="M2 6l3 3 5-6" stroke="#fff" stroke-width="2" fill="none"/></svg></span>Neuropathy</li>
        <li><span class="tick"><svg width="12" height="12" viewBox="0 0 12 12"><path d="M2 6l3 3 5-6" stroke="#fff" stroke-width="2" fill="none"/></svg></span>Muscle Strain</li>
        <li><span class="tick"><svg width="12" height="12" viewBox="0 0 12 12"><path d="M2 6l3 3 5-6" stroke="#fff" stroke-width="2" fill="none"/></svg></span>Back Spasms</li>
        <li><span class="tick"><svg width="12" height="12" viewBox="0 0 12 12"><path d="M2 6l3 3 5-6" stroke="#fff" stroke-width="2" fill="none"/></svg></span>Joint Stiffness</li>
        <li><span class="tick"><svg width="12" height="12" viewBox="0 0 12 12"><path d="M2 6l3 3 5-6" stroke="#fff" stroke-width="2" fill="none"/></svg></span>Headaches</li>
      </ul>
    </div>
  </div>
  <div class="abs video">
    <h3>Watch Our Video</h3>
    <div class="video-frame" role="img" aria-label="Video still of a laser treatment session">
      <svg class="abs" style="left:175px;top:88px" width="80" height="80" viewBox="0 0 80 80"><circle cx="40" cy="40" r="38" fill="rgba(0,0,0,.55)"/><path d="M32 24l24 16-24 16z" fill="#fff"/></svg>
      <div class="video-bar"><i></i></div>
    </div>
  </div>
</section>

<section class="section appointment">
  <div class="abs doctor" role="img" aria-label="Smiling female doctor with stethoscope"></div>
  <div class="abs booking">
    <h3>Book an Appointment</h3>
    <p>Send us your details and we will call to confirm your visit.</p>
    <div class="fields">
      <div class="field">First Name</div><div class="field">Last Name</div>
      <div class="field">Email Address</div><div class="field">Preferred Date</div>
      <div class="field wide">Phone Number</div>
      <div class="field wide msg">Message</div>
    </div>
    <div class="submit">SUBMIT</div>
  </div>
</section>

<section class="section testimonials">
  <h2>Trusted by over 25,000 Clients, every day.<br>Here's what a few had to say.</h2>
  <p class="link">See some of our customers</p>
  <div class="rule"></div>
  <div class="abs arrow" style="left:20px"><svg width="14" height="14" viewBox="0 0 14 14"><path d="M9 2L4 7l5 5" stroke="#888" stroke-width="2" fill="none"/></svg></div>
  <div class="abs arrow" style="right:20px"><svg width="14" height="14" viewBox="0 0 14 14"><path d="M5 2l5 5-5 5" stroke="#888" stroke-width="2" fill="none"/></svg></div>
  <div class="avatars">
    <div class="avatar" role="img" aria-label="Client portrait"></div>
    <div class="avatar" role="img" aria-label="Client portrait"></div>
    <div class="avatar active" role="img" aria-label="Portrait of featured client"></div>
    <div class="avatar" role="img" aria-label="Client portrait"></div>
    <div class="avatar" role="img" aria-label="Client portrait"></div>
  </div>
  <p class="t-name">Mrs. Dana Holt</p>
  <p class="t-place">Texas, United States</p>
  <p class="t-quote">After years of knee pain I could barely climb stairs. Within a few weeks of treatment I was walking every morning again. The staff were kind, patient and always explained each step of my care.</p>
</section>

<section class="section cta">
  <h2 class="abs">Need Professional Advice?</h2>
  <p class="abs">We are happy to hear what you are saying and will get you through</p>
  <div class="abs cta-phone">
    <svg width="40" height="40" viewBox="0 0 24 24"><path fill="#fff" d="M6.6 10.8a15 15 0 0 0 6.6 6.6l2.2-2.2c.3-.3.7-.4 1-.2 1.1.4 2.3.6 3.6.6.6 0 1 .4 1 1V20c0 .6-.4 1-1 1A17 17 0 0 1 3 4c0-.6.4-1 1-1h3.5c.6 0 1 .4 1 1 0 1.3.2 2.5.6 3.6.1.3 0 .7-.2 1z"/></svg>
    248-555-0142
  </div>
</section>

<footer class="section site-footer">
  <div class="abs f-col" style="left:110px">
    <h4>QUICK LINKS</h4>
    <ul><li>Home</li><li>About Us</li><li>Treatable Conditions</li><li>Testimonials</li><li>FAQs</li><li>Franchising</li><li>Contact Us</li></ul>
  </div>
  <div class="abs f-col" style="left:330px">
    <h4>FOLLOW US:</h4>
    <div class="follow"><span></span><span></span><span></span><span></span></div>
  </div>
  <div class="abs f-col" style="left:560px">
    <h4>CONTACT INFO</h4>
    <ul><li>210 Oak Avenue</li><li>Lakeside, MI 48000</li><li>248-555-0142</li><li>hello@calvexa.example</li></ul>
  </div>
  <div class="abs map" role="img" aria-label="Street map showing the clinic location">
    <svg class="abs" style="left:103px;top:50px" width="24" height="34" viewBox="0 0 24 34"><path d="M12 0a12 12 0 0 0-12 12c0 9 12 22 12 22s12-13 12-22A12 12 0 0 0 12 0z" fill="#c8121d"/><circle cx="12" cy="12" r="4" fill="#fff"/></svg>
  </div>
</footer>

<div class="section copyright">
  <span style="left:110px">Copyright 2015. All Rights Reserved</span>
  <span style="right:110px">Privacy &amp; Terms</span>
</div>

</body>
</html>
```